Business Card Design Project

My family and I are starting a small business. We need a business card designed for our Australian beef Exporting company. The business card needs to match the logo. The project I've launched is called "Logo design for an Tallow Ridge Beef Exports specifically for the China market (Contest)"

Target Market(s)

Our customer
- Chinese businessmen
- In the hospitality industry
- They value Australian produce (e.g. wine and beef)

When a consumer sees it I want them to see:
- Quality
- Tradition
- Strength, Trust and partnership
- Australian made-rustic
- Chinese business culture relevance
- Family

The above elements are important to our Chinese customer. I also want the logo to look clean and professional.

The product we're selling is:
- Exporting Australian Beef to China
- We may in the future export other meats and products too.
- Clean and green Beef

Chinese cultural relevance
- The logo must be relevant to Chinese business culture

Industry/Entity Type

Business

Font styles to use
Sans Serif

Colors
0355a3
ec1f27

Requirements
Must have
• SIDE ONE
- Include the logo: it's currently being designed by ArtHive
- Elements of the business card
Phone
Email
Mobile
Web www.tallowridgemeats.asia
Favourite Cut
Full name
Role
Text (Office locations): SYDNEY KELBARRA

Colours
- Red: similar tone in the Chinese flag
- Gold: use gold to line the logo
- Blue

SIDE 2
- Image attached of the sunrise
- add text: Kelbarra Station, Queensland, Australia

```html
<!DOCTYPE html>
<html lang="en">
<head>
<meta charset="utf-8">
<title>Tallow Ridge Beef Exports – Business Card</title>
<link href="https://fonts.googleapis.com/css2?family=Arimo:wght@700&family=Questrial&family=Open+Sans:ital,wght@1,700&family=Pinyon+Script&family=Noto+Serif+SC:wght@500&family=Noto+Sans+SC:wght@700&display=swap" rel="stylesheet">
<style>
  :root{
    --bg:#e9e4de;
    --red:#e3141c;
    --red-deep:#c40d14;
    --blue:#0b2f8a;
    --gold:#c99a2e;
    --gold-light:#f3cf6a;
    --ink:#111111;
    --night:#0e0b08;
    --card-shadow:0 10px 30px rgba(0,0,0,.25);
  }
  *{box-sizing:border-box;margin:0;padding:0}
  html,body{width:1200px;height:723px;overflow:hidden}
  body{background:var(--bg);position:relative}

  .card{position:absolute;top:70px;width:340px;height:583px;box-shadow:var(--card-shadow);overflow:hidden}

  /* Side two */
  .card-back{left:235px;background:var(--night)}
  .sunrise-photo{position:absolute;left:0;top:0;width:100%;height:62%;
    background:
      radial-gradient(ellipse at 35% 18%,#fff3c2 0%,#f6c155 14%,#d58a21 32%,transparent 60%),
      linear-gradient(180deg,#6a4a22 0%,#b7822e 28%,#8a5a1c 46%,#3a2a14 60%,#1b140c 78%,#0e0b08 100%)}
  .station-text{position:absolute;left:18px;right:22px;bottom:34px}
  .station-name{font-family:"Pinyon Script",cursive;color:var(--gold-light);font-size:18px;line-height:1.2;white-space:nowrap}
  .station-name-zh{margin-top:16px;text-align:right;font-family:"Noto Serif SC",serif;color:var(--red);font-size:21px;line-height:1.35;letter-spacing:2px}

  /* Side one */
  .card-front{left:625px;background:#fff}
  .silk-decor{position:absolute;inset:0;
    background:
      radial-gradient(ellipse at 70% 35%,rgba(214,120,140,.28),transparent 55%),
      radial-gradient(ellipse at 30% 70%,rgba(214,120,140,.22),transparent 50%),
      radial-gradient(ellipse at 80% 80%,rgba(200,90,110,.2),transparent 45%)}
  .gold-ribbon{position:absolute;right:-40px;top:-30px;width:260px;height:60px;transform:rotate(18deg);
    background:linear-gradient(90deg,rgba(201,154,46,0),var(--gold) 40%,var(--gold-light) 70%,#8a5a10)}
  .front-content{position:relative;padding:34px 20px 0 24px}
  .company-en{font-family:"Arimo",sans-serif;font-weight:700;color:var(--red);font-size:19px;white-space:nowrap}
  .company-zh{font-family:"Noto Sans SC",sans-serif;font-weight:700;color:var(--red);font-size:26px;letter-spacing:3px;margin-top:2px;white-space:nowrap}
  .logo-slot{font-family:"Questrial",sans-serif;color:var(--gold);font-size:21px;margin-top:24px;font-weight:700;white-space:nowrap}
  .holder-name{font-family:"Questrial",sans-serif;font-weight:400;color:var(--ink);font-size:24px;margin-top:26px;white-space:nowrap}
  .holder-role{font-family:"Open Sans",sans-serif;font-style:italic;font-weight:700;color:var(--red);font-size:14px;margin-top:4px;padding-left:30px}
  .contact-list{list-style:none;margin-top:22px}
  .contact-list li{display:flex;align-items:center;gap:12px;height:34px;font-family:"Open Sans",sans-serif;font-style:italic;font-weight:700;color:var(--blue);font-size:14px}
  .contact-list svg{width:26px;height:26px;fill:var(--red);flex:none}
  .red-band{position:absolute;left:0;right:0;bottom:0;height:34px;background:linear-gradient(90deg,var(--red),var(--red-deep))}
</style>
</head>
<body>
  <section class="card card-back" aria-label="Business card, side two">
    <div class="sunrise-photo" role="img" aria-label="Photograph of the sunrise over the hills at Kelbarra Station"></div>
    <div class="station-text">
      <p class="station-name">Kelbarra Station, Queensland, Australia</p>
      <p class="station-name-zh">凯尔巴拉站<br>昆士兰州<br>澳大利亚</p>
    </div>
  </section>

  <section class="card card-front" aria-label="Business card, side one">
    <div class="silk-decor" role="img" aria-label="Soft pink silk decoration"></div>
    <div class="gold-ribbon" role="img" aria-label="Gold silk ribbon"></div>
    <div class="front-content">
      <h1 class="company-en">Tallow Ridge Beef Exports</h1>
      <p class="company-zh">塔洛嶺牛肉出口公司</p>
      <p class="logo-slot">LOGO OF THE COMPANY</p>
      <h2 class="holder-name">Name Of The Card Holder</h2>
      <p class="holder-role">Post Of The Card Holder</p>
      <ul class="contact-list">
        <li><svg viewBox="0 0 24 24"><path d="M7 1h10a2 2 0 0 1 2 2v18a2 2 0 0 1-2 2H7a2 2 0 0 1-2-2V3a2 2 0 0 1 2-2zm0 3v14h10V4zm5 15.5a1 1 0 1 0 0 2 1 1 0 0 0 0-2z"/></svg>Mobile Numbers</li>
        <li><svg viewBox="0 0 24 24"><path d="M3 8c0-3 4-4 9-4s9 1 9 4v2h-5V8H8v2H3zm4 3h10l3 9H4zm5 2a3 3 0 1 0 0 6 3 3 0 0 0 0-6z"/></svg>Telephone Number</li>
        <li><svg viewBox="0 0 24 24"><path d="M6 2h10l2 2v5H6zm-3 8h18a1 1 0 0 1 1 1v8H2v-8a1 1 0 0 1 1-1zm4 6v6h10v-6z"/></svg>Fax</li>
        <li><svg viewBox="0 0 24 24"><path d="M12 1a7 7 0 0 1 7 7c0 5-7 15-7 15S5 13 5 8a7 7 0 0 1 7-7zm0 4a3 3 0 1 0 0 6 3 3 0 0 0 0-6z"/></svg>Address</li>
        <li><svg viewBox="0 0 24 24"><path d="M1 5h22v14H1zm2 2v.5l9 6 9-6V7zm0 3v7h18v-7l-9 6z"/></svg>Email Id</li>
        <li><svg viewBox="0 0 24 24"><path d="M12 1a11 11 0 1 1 0 22 11 11 0 0 1 0-22zm-3 5c-2 1-4 4-3 7l3 1 1 4 2-1 1-3 3-1-1-3-3 1-2-2 2-2z"/></svg>Website</li>
      </ul>
    </div>
    <div class="red-band"></div>
  </section>
</body>
</html>
```